Drone services brochure, offering revolutionary new SkyTally service.

We need a 8.5 x 11 tri-fold that opens up into THREE 8.5 x 11 pages (all connected as a tri-fold, of course). The trifold is going to be a sales tool we will use to sell our services to commercial roofing contractors. We want the cover of the trifold to really catch the attention or intrigue a roofing professional who we'd be pitching the service to, see the file titled "commercial cover example.png" so you get an idea of what I'm referring to The logos for Summit Lensworks and SkyTally should be next to each other, and at the TOP of the page on the cover page. All the content required is included in the file uploads, including the photos we want to use and also the written text to go with the photos. Please see the file title "Commercial-roofing SkyTally Brochure INSTRUCTIONS" for clear instructions as to what text goes where and with which photos, also see trifold examples 1-3 that give you an idea as to how I envision the layout, and finally see the actual trifold examples of a completed trifold. Finally, you will notice that all these photos are sample photos, I have not yet purchased the rights to these photos simply because I need to make sure that 1) there's enough room and 2)these are actually the photos we want to use. Once the design is set, then I'll purchase the files and send them to the designer.

Target Market(s)

Commercial roofing contractors are going to be who read/see the trifold.

Industry/Entity Type

Sales

Font styles to use
Serif

Colors
0555a3
f37022
34a6d7

Requirements
Must have
• Project must have a clean look to it that is easy on the eyes, especially the cover.
Nice to have
• I would be nice to fit all the pictures i included, even if they are minimized in size a bit.

```html
<!DOCTYPE html>
<html lang="en">
<head>
<meta charset="utf-8">
<title>Summit Lensworks – Commercial Roofing Tri-fold</title>
<link rel="stylesheet" href="https://fonts.googleapis.com/css2?family=Montserrat:wght@400;600;700;800&family=Crimson+Text:wght@400;700&display=swap">
<style>
:root{
  --page-bg:#e4e4e4;
  --navy:#2a4f8c;
  --blue:#3566ae;
  --blue-mid:#3a7bc4;
  --sky:#4aa3d8;
  --deep:#27528f;
  --paper:#ffffff;
  --light-grey:#ececec;
  --ink:#2b2b2b;
  --accent:#f37022;
}
*{box-sizing:border-box;margin:0;padding:0}
html,body{width:1200px;height:800px;overflow:hidden}
body{background:var(--page-bg);font-family:"Montserrat",Arial,sans-serif;color:var(--paper)}
.spread{position:absolute;left:30px;top:120px;width:1140px;height:560px;display:flex;box-shadow:0 10px 30px rgba(0,0,0,.18)}
.panel{position:relative;width:380px;height:560px;overflow:hidden;background:var(--paper)}
.block{position:absolute}
.photo{position:absolute}
.heading{font-weight:800;font-size:15px;text-transform:uppercase;letter-spacing:.3px;margin-bottom:6px}
.body-text{font-size:8px;line-height:1.45}
/* left panel */
.offer{left:0;top:0;width:200px;height:200px;background:var(--blue);padding:18px 14px}
.photo-rooftops{left:200px;top:0;width:180px;height:110px;background:linear-gradient(135deg,#b86a4a,#7e8a5a 55%,#c9b79a)}
.photo-solar{left:200px;top:110px;width:180px;height:90px;background:linear-gradient(160deg,#5c7fa8,#2d4f7a 60%,#9aa6b4)}
.service-band{left:0;top:200px;width:380px;height:28px;background:var(--navy);font-weight:700;font-size:10px;display:flex;align-items:center;justify-content:center;border-bottom:2px solid var(--accent)}
.roof-measure{left:0;top:228px;width:190px;height:110px;background:var(--deep);padding:12px 12px}
.photo-worker{left:190px;top:228px;width:190px;height:110px;background:linear-gradient(135deg,#5a6470,#c08e62 55%,#e7b941)}
.photo-chalkboard{left:0;top:338px;width:190px;height:110px;background:linear-gradient(160deg,#3c3c3c,#262626)}
.arrows{left:190px;top:338px;width:190px;height:110px;background:var(--light-grey);padding:12px 12px;color:var(--ink)}
.arrows .heading,.old-computer .heading{color:var(--deep)}
.old-computer{left:0;top:448px;width:190px;height:112px;background:var(--paper);padding:14px 12px;color:var(--ink)}
.photo-computer{left:190px;top:448px;width:190px;height:112px;background:linear-gradient(160deg,#d6d6d6,#a9a29a)}
/* middle panel */
.photo-lake{left:0;top:0;width:380px;height:200px;background:linear-gradient(180deg,#cfe3f3 0%,#7fa4c6 35%,#2e5e99 60%,#1d4278 100%)}
.about{left:0;top:200px;width:195px;height:225px;background:var(--blue-mid);padding:16px 13px}
.about .heading{font-size:17px}
.photo-parcel-drone{left:195px;top:200px;width:185px;height:225px;background:linear-gradient(180deg,#4b7ec0,#8ab3de 60%,#c9a47a)}
.contact{left:0;top:425px;width:380px;height:135px;background:var(--deep)}
.contact-stripe{position:absolute;left:0;top:0}
.contact-inner{position:absolute;left:0;right:0;top:30px;text-align:center}
.brand{display:inline-flex;align-items:center;gap:7px;font-family:"Montserrat",Arial,sans-serif;font-weight:700;color:var(--paper);letter-spacing:1.5px;text-transform:uppercase}
.brand-mark{width:12px;height:12px;background:var(--paper);flex:none}
.contact .brand{font-size:14px}
.contact-lines{font-size:6.5px;margin-top:8px;line-height:1.6}
.social{font-size:7px;font-weight:600;margin-top:4px}
.social-boxes{display:flex;gap:3px;justify-content:center;margin-top:3px}
.social-boxes span{width:9px;height:9px;background:var(--paper)}
/* cover panel */
.cover-brands{left:0;top:0;width:250px;height:150px;background:var(--blue);display:flex;align-items:center;justify-content:center;gap:14px;padding:0 12px}
.cover-brands .brand{font-size:11px;flex-direction:column;gap:8px;text-align:center;line-height:1.3;letter-spacing:1px}
.cover-brands .brand-mark{width:20px;height:20px}
.brand-divider{width:2px;height:62px;background:var(--accent)}
.photo-drone{left:250px;top:0;width:130px;height:150px;background:linear-gradient(180deg,#6f9bd0,#9cc0e6)}
.photo-roof-aerial{left:0;top:150px;width:175px;height:300px;background:linear-gradient(160deg,#9ea4aa,#d7d9db 50%,#6e747a)}
.headline{left:175px;top:150px;width:205px;height:300px;background:var(--sky);padding:22px 12px;text-align:center;font-family:"Crimson Text",Georgia,serif}
.headline .lead{font-size:16px}
.headline .big{font-size:27px;font-weight:700;line-height:1.05}
.headline .sub{font-size:17px;font-weight:700;line-height:1.1;margin-top:3px}
.headline .small{font-size:12px;margin-top:2px}
.headline .rule{width:46px;height:3px;background:var(--accent);margin:18px auto 0}
.headline .year{font-family:"Montserrat",Arial,sans-serif;font-weight:800;font-size:62px;letter-spacing:-2px;margin-top:14px}
.partner{left:0;top:450px;width:380px;height:110px;background:var(--navy);display:flex;flex-direction:column;align-items:center;justify-content:center;text-align:center;font-family:"Crimson Text",Georgia,serif;border-top:3px solid var(--accent)}
.partner .tag{font-size:13px}
.partner .name{font-size:21px;font-weight:700;line-height:1.1}
.partner .tail{font-size:15px}
</style>
</head>
<body>
<main class="spread">

  <section class="panel panel-services">
    <div class="block offer">
      <h2 class="heading">We Offer Our</h2>
      <p class="body-text">Services with safety, cost, and quality in mind. We save contractors time on every bid by flying licensed drones over the roof and delivering accurate measurement reports, crisp photos and detailed data that help your estimators win more work while keeping crews off the roof.</p>
    </div>
    <div class="photo photo-rooftops" role="img" aria-label="Aerial photo of residential rooftops"></div>
    <div class="photo photo-solar" role="img" aria-label="Drone flying over a roof with solar panels"></div>
    <div class="block service-band">What Summit Lensworks Can Do For Your Business</div>
    <div class="block roof-measure">
      <h3 class="heading">Roof Measure</h3>
      <p class="body-text">Supplement measurements by implementing drone imagery captured with GPS level precision, producing a high resolution model that is scaled to size, ready for your estimators.</p>
    </div>
    <div class="photo photo-worker" role="img" aria-label="Roofer in a hard hat working on a roof"></div>
    <div class="photo photo-chalkboard" role="img" aria-label="Chalkboard with rising arrows and falling costs"></div>
    <div class="block arrows">
      <h3 class="heading">Arrows</h3>
      <p class="body-text">Increase workforce safety and decrease company liability by reducing the amount of time a technician spends on the roof taking measurements and photos, all while increasing turnaround time on estimates.</p>
    </div>
    <div class="block old-computer">
      <h3 class="heading">Old Computer</h3>
      <p class="body-text">Provide estimators with up-to-date and crystal clear imagery, produced almost in real time and on demand, while your competitor is still relying on dated GeoView maps.</p>
    </div>
    <div class="photo photo-computer" role="img" aria-label="Vintage desktop computer"></div>
  </section>

  <section class="panel panel-about">
    <div class="photo photo-lake" role="img" aria-label="Aerial view of a lake among green hills"></div>
    <div class="block about">
      <h2 class="heading">About Us</h2>
      <p class="body-text">Summit Lensworks is a network of licensed, skilled, and insured drone pilots. The founders bring backgrounds in aviation, engineering and construction, and share a passion for helping roofing companies work safer. The use of drones for roof measurement began in 2016 when the technology was first applied to estimate solar panel installations. Now Summit Lensworks has grown to offer estimating services for residential and commercial roof estimating.</p>
    </div>
    <div class="photo photo-parcel-drone" role="img" aria-label="Drone carrying a cardboard parcel"></div>
    <div class="block contact">
      <svg class="contact-stripe" width="380" height="40" viewBox="0 0 380 40" aria-hidden="true">
        <polygon points="0,0 380,0 380,6 0,34" fill="#ffffff"/>
        <polygon points="0,34 380,6 380,12 0,40" fill="#4aa3d8"/>
      </svg>
      <div class="contact-inner">
        <div class="brand"><span class="brand-mark"></span>Summit Lensworks</div>
        <p class="contact-lines">info@summitlensworks.net &nbsp;|&nbsp; www.summitlensworks.net<br>P.O. Box 1420 Harbor City CA 90710</p>
        <p class="social">Social Media</p>
        <div class="social-boxes"><span></span><span></span><span></span></div>
      </div>
    </div>
  </section>

  <section class="panel panel-cover">
    <div class="block cover-brands">
      <div class="brand"><span class="brand-mark"></span>Summit<br>Lensworks</div>
      <span class="brand-divider" aria-hidden="true"></span>
      <div class="brand"><span class="brand-mark"></span>SkyTally</div>
    </div>
    <div class="photo photo-drone" role="img" aria-label="Quadcopter drone against a blue sky"></div>
    <div class="photo photo-roof-aerial" role="img" aria-label="Aerial view of a flat commercial roof"></div>
    <div class="block headline">
      <p class="lead">A Competitive</p>
      <p class="big">Advantage in</p>
      <p class="sub">Commercial Roofing</p>
      <p class="small">with on-demand</p>
      <p class="sub">Drone Imagery In</p>
      <div class="rule" aria-hidden="true"></div>
      <p class="year">2018</p>
    </div>
    <div class="block partner">
      <p class="tag">A Veteran-Owned Business</p>
      <p class="name">Bay Trade Chamber</p>
      <p class="tail">Of Commerce</p>
    </div>
  </section>

</main>
</body>
</html>
```